Update Law Firm Website

Update law firm website pages, add pages for employees. Current website looks stale. www.lowrevanlaw.com

Target Market(s)

Personal injury clients

Industry/Entity Type

Legal

Number of Pages Required

5+ page

Font styles to use
Serif

Requirements
Must have
• User friendly and engaging design
Nice to have
• ?
Should not have
• scales of justice, law books,

```html
<!DOCTYPE html>
<html lang="en">
<head>
<meta charset="utf-8">
<title>Liberty Injury Law Group</title>
<link href="https://fonts.googleapis.com/css2?family=Glegoo:wght@400;700&display=swap" rel="stylesheet">
<style>
:root{
  --accent:#e39c0c;
  --accent-bright:#f2ab1c;
  --ink:#222;
  --text:#666;
  --muted:#888;
  --band:#ebebeb;
  --line:#d6d6d6;
  --footer:#333333;
  --footer-text:#d8d8d8;
  --white:#fff;
}
*{box-sizing:border-box;margin:0;padding:0}
html,body{width:1200px;height:2397px;overflow:hidden}
body{font-family:"Glegoo",Georgia,serif;color:var(--text);background:var(--white);position:relative}
.btn{display:inline-block;background:var(--accent);color:var(--white);font-weight:700;font-size:15px;letter-spacing:.3px;text-transform:uppercase;border-radius:2px;padding:0 18px;line-height:33px;text-decoration:none}
/* header */
.site-header{height:110px;position:relative}
.brand{position:absolute;left:73px;top:30px;text-align:center}
.brand-name{font-size:18px;color:var(--ink)}
.brand-sub{font-size:14px;color:var(--muted);margin-top:6px}
.call{position:absolute;left:828px;top:37px;display:flex;align-items:center;gap:11px}
.call-icon{width:32px;height:32px;border-radius:50%;background:#eee;display:flex;align-items:center;justify-content:center}
.call-label{font-size:13px;color:var(--muted);line-height:1}
.call-number{font-size:19px;color:var(--ink);line-height:1.2}
.site-header .btn{position:absolute;left:1032px;top:40px;line-height:32px;font-size:14px;padding:0 13px}
/* nav */
.main-nav{height:47px;background:#efefef;display:flex;align-items:center;padding-left:73px;position:relative}
.main-nav a{font-size:13px;color:#555;text-decoration:none;margin-right:22px;line-height:47px;position:relative;white-space:nowrap}
.main-nav a.active:after{content:"";position:absolute;left:0;right:0;bottom:0;height:2px;background:var(--accent)}
.search{position:absolute;left:982px;top:10px;width:142px;height:28px;background:var(--white);border-radius:14px;display:flex;align-items:center;padding-left:10px;gap:6px;font-size:13px;color:#aaa}
/* hero */
.hero{height:555px;position:relative;background:linear-gradient(100deg,#4f4234 0%,#6e5c48 22%,#7d6a55 38%,#9a8b77 55%,#bdb4a6 72%,#e3ded5 88%,#efece6 100%)}
.hero-tagline{position:absolute;left:73px;top:216px;width:400px;color:var(--white);font-size:20px;line-height:30px;text-shadow:0 1px 3px rgba(0,0,0,.45)}
.hero-tagline span{color:var(--accent-bright)}
.consult{position:absolute;left:795px;top:75px;width:331px;height:408px;background:rgba(255,255,255,.93);border:3px solid rgba(255,255,255,.6);padding:30px 33px}
.consult h2{font-weight:400;font-size:21px;color:var(--ink);line-height:26px}
.consult h2 span{color:var(--accent)}
.field{border-bottom:1px solid #bbb;height:53px;display:flex;align-items:flex-end;padding-bottom:10px;font-size:13px;color:#999}
.field:first-of-type{height:55px}
.consult .btn{display:block;text-align:center;margin-top:22px;line-height:46px;font-size:14px}
/* intro */
.intro{height:513px;text-align:center;padding-top:55px}
.avatar{width:135px;height:135px;border-radius:50%;margin:0 auto;background:radial-gradient(circle at 50% 40%,#9a8a7a,#3a3530 70%)}
.section-title{font-weight:400;font-size:19px;color:var(--ink)}
.intro .section-title{margin-top:36px}
.intro p{width:700px;margin:22px auto 0;font-size:13px;line-height:24px}
.intro .btn{margin-top:30px;font-size:14px;line-height:31px}
/* liability */
.liability{height:485px;background:var(--band);text-align:center;padding-top:50px}
.liability .lead{font-size:13px;line-height:24px;width:700px;margin:16px auto 0}
.columns{display:flex;padding:0 73px;margin-top:47px;text-align:left}
.col{width:360px}
.col h3{font-weight:400;color:var(--accent);font-size:17px}
.col p{font-size:13px;line-height:24px;margin-top:14px;width:335px}
.liability .btn{margin-top:55px;font-size:14px;line-height:31px}
/* cta */
.cta{height:440px;text-align:center;padding-top:50px}
.cta .bio{width:700px;margin:0 auto;font-size:17px;line-height:28px;color:#555}
.award{width:90px;height:38px;margin:32px auto 0;background:#c79a2a;border-radius:2px}
.cta-line{font-size:21px;color:#777;margin-top:28px}
.cta-phone{font-size:37px;color:var(--ink);letter-spacing:1px;margin-top:6px}
.cta .btn{margin-top:14px;font-size:14px;line-height:31px}
/* footer */
.site-footer{height:247px;background:var(--footer);color:var(--footer-text);position:relative}
.site-footer h4{font-weight:400;font-size:17px;color:var(--white);position:absolute;top:43px}
.subscribe h4{left:73px}
.subscribe .email{position:absolute;left:73px;top:93px;width:213px;height:46px;background:var(--white);border-radius:2px;font-size:13px;color:#aaa;padding:15px 18px}
.subscribe .btn{position:absolute;left:294px;top:93px;line-height:46px;font-size:14px;padding:0 22px}
.contact h4{left:477px}
.contact address{position:absolute;left:477px;top:88px;font-style:normal;font-size:13px;line-height:23px}
.contact .tel{position:absolute;left:671px;top:88px;font-size:13px}
.contact .btn{position:absolute;left:671px;top:112px;font-size:14px;line-height:32px}
.badge-circle{position:absolute;left:845px;top:66px;width:84px;height:84px;border-radius:50%;background:radial-gradient(circle,#2a3f70 55%,#b8983e 58%,#1e2d55 64%)}
.badge-rating{position:absolute;left:953px;top:68px;width:173px;height:80px;background:var(--white);border-radius:2px}
.footer-rule{position:absolute;left:73px;right:73px;top:180px;height:1px;background:#454545}
.copyright{position:absolute;left:73px;top:206px;font-size:13px}
.social{position:absolute;right:73px;top:196px;display:flex;align-items:center;gap:7px;font-size:13px}
.social span.sq{width:33px;height:33px;background:#4a4a4a;display:inline-block;border-radius:2px}
.social .label{margin-right:8px}
</style>
</head>
<body>
<header class="site-header">
  <div class="brand">
    <div class="brand-name">Liberty Injury Law Group</div>
    <div class="brand-sub">Daniel R. Marlow, Esquire</div>
  </div>
  <div class="call">
    <span class="call-icon"><svg width="14" height="14" viewBox="0 0 24 24"><path fill="#999" d="M6.6 10.8a15 15 0 0 0 6.6 6.6l2.2-2.2c.3-.3.7-.4 1-.2 1.1.4 2.3.6 3.6.6.6 0 1 .4 1 1V20c0 .6-.4 1-1 1A17 17 0 0 1 3 4c0-.6.4-1 1-1h3.5c.6 0 1 .4 1 1 0 1.3.2 2.5.6 3.6.1.3 0 .7-.2 1z"/></svg></span>
    <div><div class="call-label">Call Us Today</div><div class="call-number">(215) 555-0142</div></div>
  </div>
  <a class="btn" href="#">Email Us</a>
</header>
<nav class="main-nav">
  <a class="active" href="#">Slip and Fall</a>
  <a href="#">Auto Accident</a>
  <a href="#">Construction Injuries</a>
  <a href="#">Medical Malpractice</a>
  <a href="#">Employees</a>
  <a href="#">Results</a>
  <a href="#">About Us</a>
  <a href="#">Contact Us</a>
  <div class="search"><svg width="12" height="12" viewBox="0 0 24 24"><circle cx="10" cy="10" r="7" fill="none" stroke="#999" stroke-width="3"/><path d="M15 15l7 7" stroke="#999" stroke-width="3"/></svg>Search</div>
</nav>
<section class="hero" role="img" aria-label="Photograph of a row of tall stone columns in a courthouse colonnade">
  <p class="hero-tagline">We take all cases on a contingency basis, meaning you will not pay attornry fees or costs unless <span>we recover on your behalf.</span></p>
  <form class="consult">
    <h2>Schedule <span>FREE</span><br>Consultation Here</h2>
    <div class="field">Name</div>
    <div class="field">Email</div>
    <div class="field">Phone</div>
    <div class="field">Case</div>
    <a class="btn" href="#">Submit</a>
  </form>
</section>
<section class="intro">
  <div class="avatar" role="img" aria-label="Portrait photo of attorney Daniel R. Marlow"></div>
  <h2 class="section-title">Affordable and Essential Legal Advocate for Your Injury Claim</h2>
  <p>When you are hit by a fatigued driver of a tractor-trailer or you suffer a fatal stroke because of a delayed diagnosis by a physician, the consequences can include staggering medical bills, debilitating pain and permanent disability. While overcoming the emotional, physical and financial hardships associated with a serious injury always present serious challenges, incidents resulting in substantial injuries can be even more traumatic when they are caused by the negligent, reckless or intentional actions of another individual, company or government entity.</p>
  <a class="btn" href="#">Learn More</a>
</section>
<section class="liability">
  <h2 class="section-title">Basis for Imposing Liability</h2>
  <p class="lead">The basis for imposing liability for damages in a personal injury lawsuit may be negligence, recklessness, intentional misconduct or strict liability.</p>
  <div class="columns">
    <div class="col"><h3>Negligence &amp; Recklessness</h3><p>Most personal injury claims are based on the law of negligence. In basic terms, negligence refers to the failure of a party to act with reasonable care which causes foreseeable injury toward another individual to whom a duty of care is owed.</p></div>
    <div class="col"><h3>Intentional Actions</h3><p>When a party commits a physical assault, battery, rape, sexual assault or other form of intentional conduct that causes injury, this type of case is referred to as an intentional tort. These cases will often merit punitive damages.</p></div>
    <div class="col"><h3>Strict Liability</h3><p>There are certain cases where an injury victim does not have to specifically prove any of the forms of misconduct indicated above. When a defective product causes injury to a consumer, for example, any party involved .</p></div>
  </div>
  <a class="btn" href="#">Learn More</a>
</section>
<section class="cta">
  <p class="bio">Daniel R. Marlow is a Philadelphia Injury Lawyer who has successfully handled death and serious injury cases involving city transit, car and trucking accidents, injuries caused by toxic chemicals, slip and fall cases involving shopping centers and office buildings, and against insurance companies.</p>
  <div class="award" role="img" aria-label="Award badge"></div>
  <p class="cta-line">For A Free Case Evaluation,&nbsp; Contact Us Today</p>
  <p class="cta-phone">(215) 555-0199</p>
  <a class="btn" href="#">Email Us</a>
</section>
<footer class="site-footer">
  <div class="subscribe">
    <h4>Subscribe Our Newsletter!</h4>
    <div class="email">Email Address</div>
    <a class="btn" href="#">Subscribe</a>
  </div>
  <div class="contact">
    <h4>Get In Touch</h4>
    <address>Daniel R. Marlow, Esquire<br>2200 Larch St #410<br>Philadelphia, PA, 19103</address>
    <div class="tel">T: (215) 555-0142</div>
    <a class="btn" href="#">Email Us</a>
  </div>
  <div class="badge-circle" role="img" aria-label="Trial lawyer association badge"></div>
  <div class="badge-rating" role="img" aria-label="Lawyer rating badge"></div>
  <div class="footer-rule"></div>
  <p class="copyright">Copyright © 2016 Liberty Injury Law Group All Rights Reserved</p>
  <div class="social"><span class="label">Connect With Us :</span><span class="sq"></span><span class="sq"></span></div>
</footer>
</body>
</html>
```